logo design and sales page for dodecahedrons

We sell dodecahedrons for meditation purpose. These are copper objects where you sit in (may sound strange for some of you, but it gives you a great effect).
We have a template for wordpress installed on our webserver (see https://lumivorn.at/) where we like the basic design (colour scheme) and functionality.
So we would need a Logo that is mainly comprising a dodecahedron, and if a sample picture can be made, it would be great to have a person sitting in a dodecahedron whereas the enery is visualized (see sample stock pictures).
Please check: C60_-_4_1630513838 to see the specifications of the dodecahedron.

Target Market(s)

People familiar with meditation practice, looking for inner peace and spiritual connection

Industry/Entity Type

Meditation, Yoga, Energy work, spiritual

Font styles to use
Sans Serif

Colors
F0912C
F2A743
F7CA91
FBE8D2
FDF5EE

Requirements
Must have
• The dodecahedron as a logo
Nice to have
• A person meditationg in a dodecahedron whereas the enery is visualized (see sample stock pictures)

```html
<!DOCTYPE html>
<html lang="en">
<head>
<meta charset="utf-8">
<title>Lumivorn</title>
<link href="https://fonts.googleapis.com/css2?family=Poppins:wght@500;600;700&family=Roboto:wght@400;500;700&display=swap" rel="stylesheet">
<style>
:root{
  --orange:#F0912C;
  --orange-2:#F2A743;
  --orange-3:#F7CA91;
  --orange-4:#FBE8D2;
  --orange-5:#FDF5EE;
  --ink:#1c1c1c;
  --text:#6f6f6f;
  --grey-bg:#f3f3f3;
  --footer:#454545;
  --white:#ffffff;
}
*{margin:0;padding:0;box-sizing:border-box}
html,body{width:1200px;height:4751px;overflow:hidden}
body{font-family:'Roboto',sans-serif;color:var(--ink);background:var(--white);position:relative}
section,header,footer{position:absolute;left:0;width:1200px}
.abs{position:absolute}
.h2{position:absolute;left:0;width:1200px;text-align:center;font-family:'Poppins',sans-serif;font-weight:600;font-size:32px;color:var(--ink)}
.h2::after{content:"";display:block;width:40px;height:3px;background:var(--orange);margin:14px auto 0}

/* hero */
.hero{top:0;height:643px;background:linear-gradient(100deg,#f28a1e 0%,#f5a022 55%,#f6b42a 80%,#ef6a2c 100%);overflow:hidden}
.hero-art{position:absolute;left:560px;top:0;width:640px;height:643px;background:radial-gradient(ellipse 190px 300px at 280px 420px,rgba(58,26,8,.95) 0%,rgba(58,26,8,.85) 60%,rgba(58,26,8,0) 100%),radial-gradient(circle at 280px 150px,#fff6e8 0%,#fbe0b8 18%,rgba(247,202,145,.5) 34%,rgba(240,145,44,0) 55%)}
.brand{position:absolute;left:110px;top:24px;display:flex;align-items:center;gap:12px;color:var(--white);font-family:'Poppins',sans-serif;font-weight:600;font-size:20px}
.brand .mark{width:52px;height:52px;border-radius:50%;border:2px solid var(--white)}
.nav{position:absolute;right:112px;top:41px;display:flex;gap:28px;font-size:13px;font-weight:500;color:var(--white)}
.hero-title{position:absolute;left:108px;top:262px;font-family:'Poppins',sans-serif;font-weight:700;font-size:52px;color:var(--white);letter-spacing:.5px}
.hero-text{position:absolute;left:110px;top:348px;width:470px;color:var(--white);font-size:15px;line-height:24px;font-weight:500}
.btn{position:absolute;left:110px;top:427px;width:157px;height:47px;background:var(--orange-2);color:var(--white);font-size:13px;font-weight:700;display:flex;align-items:center;justify-content:center;gap:8px;border-radius:2px}

/* welcome */
.welcome{top:643px;height:702px}
.feature{position:absolute;width:276px;height:90px;border-radius:45px;background:var(--white);box-shadow:0 3px 14px rgba(0,0,0,.1);display:flex;align-items:center;gap:14px;padding:0 10px}
.feature .ic{width:72px;height:72px;border-radius:50%;background:var(--orange);flex:none;display:flex;align-items:center;justify-content:center}
.feature h4{font-size:11px;font-weight:700;margin-bottom:6px}
.feature p{font-size:11.5px;color:var(--text);line-height:18px}
.feature.left{flex-direction:row-reverse;text-align:center}
.feature .txt{flex:1}
.core{position:absolute;left:468px;top:240px;width:260px;height:260px;border-radius:50%;background:radial-gradient(circle at 50% 45%,#ffffff 0%,#e6e6e6 40%,#cfcfcf 55%,#f7f7f7 70%)}

/* what we do */
.what{top:1345px;height:494px}
.what-img{position:absolute;left:0;top:0;width:581px;height:494px;background:radial-gradient(circle at 270px 240px,#e8a53a 0%,#8a5a2a 25%,#4a4e56 55%,#2e3138 100%)}
.what-title{position:absolute;left:676px;top:40px;font-family:'Poppins',sans-serif;font-weight:600;font-size:32px}
.what-title::after{content:"";display:block;width:40px;height:3px;background:var(--orange);margin-top:10px}
.what-item{position:absolute;left:675px;display:flex;gap:22px}
.what-item h4{font-size:13px;font-weight:700;margin:6px 0 6px}
.what-item p{font-size:13px;color:var(--text);line-height:17px;width:290px}

/* portfolio */
.portfolio{top:1935px;height:730px;background:var(--grey-bg)}
.grid{position:absolute;left:110px;top:168px;display:grid;grid-template-columns:repeat(3,317px);grid-auto-rows:232px;gap:14px 13px}
.tile{width:317px;height:232px}
.t1{background:radial-gradient(circle at 50% 60%,#0b1630,#1d5fb8 60%,#3aa0f0)}
.t2{background:radial-gradient(circle at 50% 70%,#e8b070,#203a70 40%,#0a1330)}
.t3{background:radial-gradient(circle at 50% 70%,#bfe4f8,#2f78b8 45%,#0b1b40)}
.t4{background:radial-gradient(circle at 50% 50%,#7fa8e0,#1f3d9a 50%,#0a1850)}
.t5{background:radial-gradient(circle at 50% 45%,#ff7ad8,#f4c15a 40%,#e0dcd2 75%)}
.t6{background:linear-gradient(180deg,#1a2a5a,#6a7aa8 45%,#f2b04a 80%,#3a2a1a)}

/* values */
.values{top:2665px;height:446px}
.value{position:absolute;top:170px;width:245px;text-align:center}
.value h4{font-size:13px;font-weight:700;margin-top:14px}
.value .num{font-family:'Poppins',sans-serif;font-size:27px;font-weight:600;color:var(--orange);margin-top:8px}
.vdiv{position:absolute;top:190px;width:1px;height:70px;background:#e4e4e4}

/* blog */
.blog{top:3111px;height:593px;background:var(--orange)}
.blog .h2{color:var(--white)}
.blog .h2::after{background:var(--white)}
.card{position:absolute;top:164px;width:287px;height:352px;background:var(--white);border:5px solid var(--white);text-align:center}
.card .img{height:166px;position:relative}
.card .date{position:absolute;left:50%;bottom:-31px;margin-left:-31px;width:62px;height:62px;border-radius:50%;background:var(--orange);border:3px solid var(--white);color:var(--white);font-size:11px;font-weight:500;line-height:14px;display:flex;flex-direction:column;justify-content:center}
.card h4{font-size:13px;font-weight:700;margin-top:48px}
.card p{font-size:13px;color:var(--text);line-height:24px;margin:12px 14px 0}
.b1{background:linear-gradient(135deg,#b9b2aa,#6e6863 50%,#d8d4cf)}
.b2{background:radial-gradient(circle at 50% 55%,#f4e24a,#e03aa8 30%,#1a2a70 60%,#0a0a18)}
.b3{background:radial-gradient(circle at 50% 55%,#7d8df0,#2730a8 45%,#0c1050)}

/* why */
.why{top:3704px;height:535px}
.why-item{position:absolute;top:175px;width:300px;text-align:center}
.why-item .ring{width:140px;height:140px;border-radius:50%;border:3px solid var(--orange);margin:0 auto;display:flex;align-items:center;justify-content:center}
.why-item .ring span{width:110px;height:110px;border-radius:50%;display:block}
.why-item h4{font-size:13px;font-weight:700;margin-top:28px}
.why-item p{font-size:13px;color:var(--text);line-height:22px;margin-top:10px}

/* footer */
.footer{top:4239px;height:512px;background:var(--footer);color:var(--white)}
.nl-title{position:absolute;left:177px;top:68px;font-size:19px;font-weight:700}
.nl-form{position:absolute;left:477px;top:59px;width:544px;height:46px;display:flex;border:1px solid var(--orange)}
.nl-form .field{flex:1;background:var(--white);display:flex;align-items:center;gap:14px;padding-left:22px;font-size:13px;color:#888}
.nl-form .go{width:140px;background:var(--orange);display:flex;align-items:center;justify-content:center;font-size:14px;font-weight:700}
.rule{position:absolute;left:110px;width:978px;height:1px;background:#6a6a6a}
.f-brand{position:absolute;left:110px;top:204px;display:flex;align-items:center;gap:12px;font-family:'Poppins',sans-serif;font-weight:600;font-size:20px}
.f-brand .mark{width:56px;height:56px;border-radius:50%;border:2px solid var(--white)}
.f-about{position:absolute;left:110px;top:286px;width:285px;font-size:13px;line-height:21px;text-align:justify}
.socials{position:absolute;left:110px;top:366px;display:flex;gap:8px}
.socials span{width:32px;height:32px;border-radius:50%;border:2px solid var(--white)}
.f-head{position:absolute;top:225px;font-size:13px;font-weight:700;text-decoration:underline}
.contact-row{position:absolute;left:474px;display:flex;align-items:center;gap:20px;font-size:13px;line-height:18px}
.contact-row svg{flex:none}
.links{position:absolute;top:256px;list-style:none;font-size:13px}
.links li{height:32px;display:flex;gap:14px}
.links li::before{content:"»";font-weight:700}
.copy{position:absolute;left:0;top:4716px;width:1200px;text-align:center;font-size:13px;color:var(--white)}
</style>
</head>
<body>

<header class="hero">
  <div class="hero-art" role="img" aria-label="Silhouette of a person meditating in lotus pose before a glowing sun"></div>
  <div class="brand"><span class="mark"></span>LUMIVORN</div>
  <nav class="nav"><span>HOME</span><span>ABOUT</span><span>PAGES</span><span>PORTFOLIO</span><span>BLOG</span><span>SHOP</span><span>CONTACT</span></nav>
  <h1 class="hero-title">LUMIVORN</h1>
  <p class="hero-text">Sed ut perspiciatis unde omnis iste natus error sit voluptatem accusantium doloremque laudantium, totam rem aperiam,</p>
  <div class="btn">GET STARTED
    <svg width="13" height="13" viewBox="0 0 13 13"><circle cx="6.5" cy="6.5" r="6.5" fill="#fff"/><path d="M5 3.5l3 3-3 3" stroke="#F0912C" stroke-width="1.8" fill="none"/></svg>
  </div>
</header>

<section class="welcome">
  <h2 class="h2" style="top:82px">Welcome to Lumivorn</h2>
  <svg class="abs" style="left:392px;top:180px" width="416" height="420" viewBox="0 0 416 420">
    <path d="M70 70 A196 196 0 0 1 346 70" stroke="#F0912C" stroke-width="4" stroke-dasharray="2 6" stroke-linecap="round" fill="none"/>
    <path d="M70 350 A196 196 0 0 0 346 350" stroke="#F0912C" stroke-width="4" stroke-dasharray="2 6" stroke-linecap="round" fill="none"/>
    <path d="M60 80 A196 196 0 0 0 70 350" stroke="#F0912C" stroke-width="3" fill="none"/>
    <path d="M356 80 A196 196 0 0 1 346 350" stroke="#F0912C" stroke-width="3" fill="none"/>
    <circle cx="208" cy="215" r="160" fill="#F0912C"/>
    <circle cx="206" cy="200" r="148" fill="#ececec"/>
    <g fill="#fff" stroke="#F0912C" stroke-width="3">
      <circle cx="62" cy="86" r="10"/><circle cx="354" cy="86" r="10"/>
      <circle cx="18" cy="216" r="10"/><circle cx="398" cy="216" r="10"/>
      <circle cx="74" cy="345" r="10"/><circle cx="342" cy="345" r="10"/>
    </g>
  </svg>
  <div class="core" role="img" aria-label="White faceted polyhedron sphere on a light pedestal"></div>

  <div class="feature left" style="left:110px;top:199px"><div class="ic"><svg width="34" height="34" viewBox="0 0 34 34"><circle cx="17" cy="17" r="11" fill="none" stroke="#fff" stroke-width="3"/></svg></div><div class="txt"><h4>LOREM IPSUM DOLOR</h4><p>Lorem ipsum dolor sit amet<br>consectetur adipiscing</p></div></div>
  <div class="feature left" style="left:65px;top:334px"><div class="ic"><svg width="34" height="34" viewBox="0 0 34 34"><path d="M17 6c5 6 5 14 0 20-5-6-5-14 0-20zM4 14c7 1 11 6 13 12-7 0-12-4-13-12zM30 14c-7 1-11 6-13 12 7 0 12-4 13-12z" fill="#fff"/></svg></div><div class="txt"><h4>LOREM IPSUM DOLOR</h4><p>Lorem ipsum dolor sit amet<br>consectetur adipiscing</p></div></div>
  <div class="feature left" style="left:125px;top:463px"><div class="ic"><svg width="34" height="34" viewBox="0 0 34 34"><circle cx="17" cy="17" r="11" fill="none" stroke="#fff" stroke-width="3"/></svg></div><div class="txt"><h4>LOREM IPSUM DOLOR</h4><p>Lorem ipsum dolor sit amet<br>consectetur adipiscing</p></div></div>
  <div class="feature right" style="left:805px;top:199px"><div class="ic"><svg width="34" height="34" viewBox="0 0 34 34"><path d="M17 6c5 6 5 14 0 20-5-6-5-14 0-20zM4 14c7 1 11 6 13 12-7 0-12-4-13-12zM30 14c-7 1-11 6-13 12 7 0 12-4 13-12z" fill="#fff"/></svg></div><div class="txt"><h4>LOREM IPSUM DOLOR</h4><p>Lorem ipsum dolor sit amet<br>consectetur adipiscing</p></div></div>
  <div class="feature right" style="left:857px;top:334px"><div class="ic"><svg width="34" height="34" viewBox="0 0 34 34"><circle cx="17" cy="17" r="11" fill="none" stroke="#fff" stroke-width="3"/></svg></div><div class="txt"><h4>LOREM IPSUM DOLOR</h4><p>Lorem ipsum dolor sit amet<br>consectetur adipiscing</p></div></div>
  <div class="feature right" style="left:802px;top:463px"><div class="ic"><svg width="34" height="34" viewBox="0 0 34 34"><path d="M17 6l12 22H5z" fill="none" stroke="#fff" stroke-width="3"/></svg></div><div class="txt"><h4>LOREM IPSUM DOLOR</h4><p>Lorem ipsum dolor sit amet<br>consectetur adipiscing</p></div></div>
</section>

<section class="what">
  <div class="what-img" role="img" aria-label="Glowing golden geodesic sphere standing in a dark room"></div>
  <h2 class="what-title">What We Do</h2>
  <div class="what-item" style="top:122px"><svg width="58" height="60" viewBox="0 0 58 60"><polygon points="29,0 55,15 55,45 29,60 3,45 3,15" fill="#F0912C"/><circle cx="29" cy="30" r="10" fill="none" stroke="#fff" stroke-width="3"/></svg><div><h4>LOREM IPSUM DOLOR</h4><p>Sed ut perspiciatis unde omnis iste natus error sit voluptatem accusantium</p></div></div>
  <div class="what-item" style="top:212px"><svg width="58" height="60" viewBox="0 0 58 60"><polygon points="29,0 55,15 55,45 29,60 3,45 3,15" fill="#F0912C"/><path d="M29 18c4 5 4 11 0 16-4-5-4-11 0-16zM18 25c6 1 9 5 11 9-6 0-10-3-11-9zM40 25c-6 1-9 5-11 9 6 0 10-3 11-9z" fill="#fff"/></svg><div><h4>LOREM IPSUM DOLOR</h4><p>Sed ut perspiciatis unde omnis iste natus error sit voluptatem accusantium</p></div></div>
  <div class="what-item" style="top:302px"><svg width="58" height="60" viewBox="0 0 58 60"><polygon points="29,0 55,15 55,45 29,60 3,45 3,15" fill="#F0912C"/><circle cx="29" cy="30" r="10" fill="none" stroke="#fff" stroke-width="3"/></svg><div><h4>LOREM IPSUM DOLOR</h4><p>Sed ut perspiciatis unde omnis iste natus error sit voluptatem accusantium</p></div></div>
  <div class="what-item" style="top:392px"><svg width="58" height="60" viewBox="0 0 58 60"><polygon points="29,0 55,15 55,45 29,60 3,45 3,15" fill="#F0912C"/><path d="M29 18l10 20H19z" fill="none" stroke="#fff" stroke-width="3"/></svg><div><h4>LOREM IPSUM DOLOR</h4><p>Sed ut perspiciatis unde omnis iste natus error sit voluptatem accusantium</p></div></div>
</section>

<section class="portfolio">
  <h2 class="h2" style="top:74px">Our Portfolio</h2>
  <div class="grid">
    <div class="tile t1" role="img" aria-label="Meditating silhouette surrounded by blue lightning"></div>
    <div class="tile t2" role="img" aria-label="Person meditating under a starry night sky with glowing light"></div>
    <div class="tile t3" role="img" aria-label="Meditating figure in front of a blue nebula"></div>
    <div class="tile t4" role="img" aria-label="Meditating figure with atom orbits over water at night"></div>
    <div class="tile t5" role="img" aria-label="Meditating figure with glowing chakra colours"></div>
    <div class="tile t6" role="img" aria-label="Meditating silhouette beneath a moonlit sky and clouds"></div>
  </div>
</section>

<section class="values">
  <h2 class="h2" style="top:80px">Our Values</h2>
  <div class="value" style="left:110px"><svg width="90" height="92" viewBox="0 0 90 92"><polygon points="45,3 84,25 84,67 45,89 6,67 6,25" fill="none" stroke="#F0912C" stroke-width="3"/><path d="M45 28c6 6 6 14 0 20-6-6-6-14 0-20zM26 52h38v6H26z" fill="#F0912C"/></svg><h4>CUSTOMIZATIONS ADDED</h4><div class="num">4589</div></div>
  <div class="vdiv" style="left:371px"></div>
  <div class="value" style="left:355px"><svg width="90" height="92" viewBox="0 0 90 92"><polygon points="45,3 84,25 84,67 45,89 6,67 6,25" fill="none" stroke="#F0912C" stroke-width="3"/><circle cx="45" cy="46" r="14" fill="none" stroke="#F0912C" stroke-width="4"/></svg><h4>THEME LOVERS</h4><div class="num">4589</div></div>
  <div class="vdiv" style="left:595px"></div>
  <div class="value" style="left:600px"><svg width="90" height="92" viewBox="0 0 90 92"><polygon points="45,3 84,25 84,67 45,89 6,67 6,25" fill="none" stroke="#F0912C" stroke-width="3"/><circle cx="45" cy="34" r="8" fill="none" stroke="#F0912C" stroke-width="3.5"/><circle cx="32" cy="56" r="8" fill="none" stroke="#F0912C" stroke-width="3.5"/><circle cx="58" cy="56" r="8" fill="none" stroke="#F0912C" stroke-width="3.5"/></svg><h4>MEDITATION</h4><div class="num">4589</div></div>
  <div class="vdiv" style="left:840px"></div>
  <div class="value" style="left:845px"><svg width="90" height="92" viewBox="0 0 90 92"><polygon points="45,3 84,25 84,67 45,89 6,67 6,25" fill="none" stroke="#F0912C" stroke-width="3"/><path d="M27 50h36l-5 12H32z" fill="#F0912C"/><circle cx="45" cy="36" r="7" fill="#F0912C"/></svg><h4>HAPPY CLIENTS</h4><div class="num">4589</div></div>
</section>

<section class="blog">
  <h2 class="h2" style="top:66px">Latest Blog</h2>
  <article class="card" style="left:133px"><div class="img b1" role="img" aria-label="Armchair inside a wooden frame structure in a bright room"><div class="date">SEP<br>2021</div></div><h4>LOREM IPSUM DOLOR SIT AMET</h4><p>Sed ut perspiciatis unde omnis iste natus error sit voluptatem accusantium doloremque laudantium, totam rem</p></article>
  <article class="card" style="left:456px"><div class="img b2" role="img" aria-label="Colourful glowing energy figure in meditation"><div class="date">SEP<br>2021</div></div><h4>LOREM IPSUM DOLOR SIT AMET</h4><p>Sed ut perspiciatis unde omnis iste natus error sit voluptatem accusantium doloremque laudantium, totam rem</p></article>
  <article class="card" style="left:778px"><div class="img b3" role="img" aria-label="Blue digital energy figure in meditation"><div class="date">SEP<br>2021</div></div><h4>LOREM IPSUM DOLOR SIT AMET</h4><p>Sed ut perspiciatis unde omnis iste natus error sit voluptatem accusantium doloremque laudantium, totam rem</p></article>
</section>

<section class="why">
  <h2 class="h2" style="top:80px">Why Choose US</h2>
  <div class="why-item" style="left:134px"><div class="ring"><span role="img" aria-label="Illustration of a woman meditating with plants" style="background:radial-gradient(circle,#fbe8d2,#f4f4f4)"></span></div><h4>LOREM IPSUM DOLOR SIT</h4><p>Sed ut perspiciatis unde omnis iste natus error sit voluptatem accusantium doloremque laudantium, totam rem</p></div>
  <div class="why-item" style="left:450px"><div class="ring"><span role="img" aria-label="Illustration of a man meditating before a yellow sun" style="background:radial-gradient(circle,#f6c230 45%,#fbe8d2 46%)"></span></div><h4>LOREM IPSUM DOLOR SIT</h4><p>Sed ut perspiciatis unde omnis iste natus error sit voluptatem accusantium doloremque laudantium, totam rem</p></div>
  <div class="why-item" style="left:766px"><div class="ring"><span role="img" aria-label="Illustration of a person meditating in green clothes" style="background:radial-gradient(circle,#d8efe0,#f6f6f6)"></span></div><h4>LOREM IPSUM DOLOR SIT</h4><p>Sed ut perspiciatis unde omnis iste natus error sit voluptatem accusantium doloremque laudantium, totam rem</p></div>
</section>

<footer class="footer">
  <div class="nl-title">SIGN UP FOR NEWSLETTER</div>
  <div class="nl-form">
    <div class="field"><svg width="16" height="12" viewBox="0 0 16 12"><rect x="1" y="1" width="14" height="10" fill="none" stroke="#F0912C" stroke-width="1.5"/><path d="M1 1l7 6 7-6" fill="none" stroke="#F0912C" stroke-width="1.5"/></svg>Enter Your Email</div>
    <div class="go">SUBSCRIBE</div>
  </div>
  <div class="rule" style="top:153px"></div>

  <div class="f-brand"><span class="mark"></span>LUMIVORN</div>
  <p class="f-about">Ut enim ad minima veniam, quis nostrum exercitationem ulla corporis suscipit laboriosam, nisi ut aliquid.</p>
  <div class="socials"><span></span><span></span><span></span><span></span></div>

  <div class="f-head" style="left:474px">CONTACT US</div>
  <div class="contact-row" style="top:268px"><svg width="28" height="28" viewBox="0 0 28 28"><circle cx="14" cy="14" r="13" fill="none" stroke="#fff" stroke-width="1.5"/><path d="M14 21s-5-5-5-9a5 5 0 0 1 10 0c0 4-5 9-5 9z" fill="none" stroke="#fff" stroke-width="1.5"/><circle cx="14" cy="12" r="1.8" fill="#fff"/></svg><span>Ferngate Court, 42 Alder Lane,<br>United States</span></div>
  <div class="contact-row" style="top:330px"><svg width="28" height="28" viewBox="0 0 28 28"><circle cx="14" cy="14" r="13" fill="none" stroke="#fff" stroke-width="1.5"/><rect x="8" y="10" width="12" height="9" fill="none" stroke="#fff" stroke-width="1.5"/><path d="M8 10l6 5 6-5" fill="none" stroke="#fff" stroke-width="1.5"/></svg><span>info@lumivorn.co.uk</span></div>
  <div class="contact-row" style="top:385px"><svg width="28" height="28" viewBox="0 0 28 28"><circle cx="14" cy="14" r="13" fill="none" stroke="#fff" stroke-width="1.5"/><path d="M10 8l3 3-2 2c1 2 2 3 4 4l2-2 3 3-2 2c-5 0-10-5-10-10z" fill="#fff"/></svg><span style="font-size:19px;font-weight:700">1 555 010 200</span></div>

  <div class="f-head" style="left:772px">QUICK LINKS</div>
  <ul class="links" style="left:772px"><li>Home</li><li>About Us</li><li>What we Do</li><li>Latest News</li><li>Reviews</li></ul>
  <div class="f-head" style="left:958px">OTHER LINKS</div>
  <ul class="links" style="left:958px"><li>Contact Us</li><li>FAQ</li><li>Help Service</li><li>Terms Of Use</li><li>Privacy Policy</li></ul>

  <div class="rule" style="top:444px"></div>
</footer>
<div class="copy">© 2021 Lumivorn. All Rights Reserved</div>

</body>
</html>
```